Edgy rebranded biz cards KRB

We are rebranding our 20 yr old mortgage company with a new logo and would like cards to compliment our new look.

Target Market(s)

potential home buyers or clients for refinance

Industry/Entity Type

Mortgage Brokerage

Contact Information for Business Card

418 W. Lomita Ave #305
Henderson, NV 89152
702.519.4827 o
702-519-4829 f
www.kestrelridgelending,example
nmls 842019
KRB is an equal housing lender

Font styles to use
Sans Serif

Colors
0455a3
3176b5
0393ce
33a6d7

Requirements
Must have
• space for a photo
Nice to have
• One side with the company info and the other with the person's info

```html
<!DOCTYPE html>
<html lang="en">
<head>
<meta charset="utf-8">
<title>Kestrel Ridge Lending – Business Cards</title>
<link rel="stylesheet" href="https://fonts.googleapis.com/css2?family=Heebo:wght@400;500&family=Montserrat:wght@500;700;800&display=swap">
<style>
  :root {
    --stage: #cccccc;
    --paper: #ffffff;
    --brand-deep: #0455a3;
    --brand-mid: #3176b5;
    --brand-bright: #0393ce;
    --brand-light: #33a6d7;
    --card-blue: #0f76bf;
    --ink-grey: #5f6164;
    --rule-grey: #86878a;
  }
  * { margin: 0; padding: 0; box-sizing: border-box; }
  html, body { width: 1062px; height: 1200px; overflow: hidden; background: var(--stage); }
  .stage { position: relative; width: 1062px; height: 1200px; }
  .card { position: absolute; left: 146px; width: 805px; height: 461px; display: block; }
  .card--company { top: 94px; }
  .card--person { top: 587px; }
  .contact-text { font-family: "Heebo", sans-serif; font-size: 15px; fill: var(--paper); letter-spacing: 0.3px; }
  .contact-text--dark { font-size: 13.5px; fill: var(--ink-grey); }
  .brand-name { font-family: "Montserrat", sans-serif; font-weight: 800; text-anchor: middle; }
  .person-name { font-family: "Montserrat", sans-serif; font-weight: 800; font-size: 21px; fill: var(--card-blue); letter-spacing: 0.8px; }
  .person-role { font-family: "Montserrat", sans-serif; font-weight: 500; font-size: 14.5px; fill: var(--rule-grey); letter-spacing: 2.5px; }
</style>
</head>
<body>
<main class="stage">

  <!-- Company side -->
  <svg class="card card--company" viewBox="0 0 805 461" aria-label="Company card">
    <defs>
      <linearGradient id="company-panel" x1="1" y1="0" x2="0.3" y2="0.8">
        <stop offset="0" stop-color="var(--brand-bright)"/>
        <stop offset="0.7" stop-color="var(--brand-deep)"/>
      </linearGradient>
    </defs>
    <rect class="card-base" width="805" height="461" fill="var(--paper)"/>
    <polygon class="panel" points="532,0 805,0 805,461 532,461 406,230" fill="url(#company-panel)"/>
    <polyline class="panel-edge" points="526,0 397,230 529,461" fill="none" stroke="var(--brand-light)" stroke-width="3"/>

    <g class="brand-lockup">
      <text class="brand-name" x="208" y="222" font-size="58" fill="var(--card-blue)">KESTREL</text>
      <text class="brand-name" x="208" y="262" font-size="30" fill="var(--card-blue)" letter-spacing="4">RIDGE LENDING</text>
    </g>

    <g class="contact-list" fill="var(--paper)">
      <path class="icon-pin" d="M532,114 a8,8 0 0 1 16,0 c0,7 -8,16 -8,16 c0,0 -8,-9 -8,-16z M540,110 a3.5,3.5 0 1 0 0.01,0z" fill-rule="evenodd"/>
      <text class="contact-text" x="554" y="125">418 W. Lomita Ave #305</text>
      <text class="contact-text" x="554" y="148">Henderson, NV 89152</text>

      <g class="icon-phone">
        <rect x="525" y="180" width="6" height="17" rx="2"/>
        <rect x="533" y="179" width="12" height="18" rx="2"/>
        <path d="M528,197 v5 a2,2 0 0 0 4,0" fill="none" stroke="var(--paper)" stroke-width="1.5"/>
      </g>
      <text class="contact-text" x="554" y="194">OFFICE: 702.519.4827 O</text>

      <g class="icon-fax">
        <rect x="530" y="221" width="12" height="10"/>
        <rect x="526" y="229" width="21" height="11" rx="1"/>
        <rect x="522" y="230" width="3" height="9"/>
      </g>
      <text class="contact-text" x="554" y="240">FAX: 702-519-4829</text>

      <g class="icon-globe" fill="none" stroke="var(--paper)" stroke-width="1.3">
        <circle cx="537" cy="286" r="11"/>
        <ellipse cx="537" cy="286" rx="5" ry="11"/>
        <line x1="526" y1="286" x2="548" y2="286"/>
        <line x1="528" y1="280" x2="546" y2="280"/>
        <line x1="528" y1="292" x2="546" y2="292"/>
      </g>
      <text class="contact-text" x="554" y="285">www.kestrelridgelending.example</text>
      <text class="contact-text" x="554" y="308">nmls 842019</text>
      <text class="contact-text" x="554" y="331">KRB is an equal housing lender</text>
    </g>
  </svg>

  <!-- Person side -->
  <svg class="card card--person" viewBox="0 0 805 461" aria-label="Personal card">
    <rect class="card-base" width="805" height="461" fill="var(--paper)"/>
    <polygon class="panel" points="475,0 805,0 805,461 451,461 341,252" fill="var(--card-blue)"/>
    <polyline class="panel-edge" points="467,0 326,252 443,461" fill="none" stroke="var(--rule-grey)" stroke-width="4"/>

    <g class="portrait">
      <circle cx="106" cy="104" r="71.5" fill="none" stroke="var(--card-blue)" stroke-width="1"/>
      <circle cx="106" cy="104" r="67" fill="#7c7e82" role="img" aria-label="Portrait photo of the owner"/>
    </g>

    <rect class="name-accent" x="0" y="195" width="5" height="31" fill="var(--card-blue)"/>
    <text class="person-name" x="43" y="212">DALEN VORHESS M.S</text>
    <text class="person-role" x="43" y="233">OWNER</text>
    <line class="divider" x1="43" y1="252" x2="326" y2="252" stroke="#c4c4c4" stroke-width="1.2"/>

    <g class="contact-list" fill="var(--card-blue)">
      <path class="icon-pin" d="M42,285 a7,7 0 0 1 14,0 c0,6 -7,14 -7,14 c0,0 -7,-8 -7,-14z M49,282 a3,3 0 1 0 0.01,0z" fill-rule="evenodd"/>
      <text class="contact-text contact-text--dark" x="70" y="288">418 W. Lomita Ave #305</text>
      <text class="contact-text contact-text--dark" x="70" y="306">Henderson, NV 89152</text>

      <g class="icon-phone">
        <rect x="40" y="334" width="5" height="15" rx="2"/>
        <rect x="47" y="333" width="11" height="16" rx="2"/>
        <path d="M42,349 v4 a2,2 0 0 0 4,0" fill="none" stroke="var(--card-blue)" stroke-width="1.4"/>
      </g>
      <text class="contact-text contact-text--dark" x="70" y="348">702.519.4827</text>

      <g class="icon-globe" fill="none" stroke="var(--card-blue)" stroke-width="1.2">
        <circle cx="50" cy="387" r="10"/>
        <ellipse cx="50" cy="387" rx="4.5" ry="10"/>
        <line x1="40" y1="387" x2="60" y2="387"/>
        <line x1="42" y1="381" x2="58" y2="381"/>
        <line x1="42" y1="393" x2="58" y2="393"/>
      </g>
      <text class="contact-text contact-text--dark" x="70" y="392">info@dalenvorhess.example</text>
    </g>

    <g class="brand-lockup">
      <text class="brand-name" x="604" y="218" font-size="58" fill="var(--paper)">KESTREL</text>
      <text class="brand-name" x="604" y="258" font-size="30" fill="var(--paper)" letter-spacing="4">RIDGE LENDING</text>
    </g>
  </svg>

</main>
</body>
</html>
```